Builders Worksite Corflute Outdoor Sign

We are a building company who are just branching out into new construction. How first new build is our own home which was designed by us and a local architect. We are proud and want to create more advertisement around our business.

We need a corflute sign that can staked outside the construction site and can be seen by people passing by.
Updates

Can we please make the company name and logo bigger (Tidewater Ridge Homes) This needs to be the focus. Can we please replace 'Manu' with 'Contact Us on 021-574-3619'

Target Market(s)

Home owners and people wishing to build on lifestyle blocks in New Zealand.

Font styles to use
Sans Serif

Requirements
Must have
• It needs to feature our:
Logo
Company name
Contact name and number - Manu - 0215743619
Landscape NOT portrait.

```html
<!DOCTYPE html>
<html lang="en">
<head>
<meta charset="utf-8">
<title>Tidewater Ridge Homes – Site Sign</title>
<link rel="stylesheet" href="https://fonts.googleapis.com/css2?family=Jost:wght@300;400;500;600&display=swap">
<style>
  :root {
    --navy-deep: #1d2336;
    --navy-mid: #273048;
    --navy-light: #3a4763;
    --gold: #f0b400;
    --white: #ffffff;
    --ink: #1e2435;
    --backdrop: #e4e4e4;
    --faint: rgba(58, 71, 99, 0.08);
  }
  * { margin: 0; padding: 0; box-sizing: border-box; }
  html, body {
    width: 1200px;
    height: 1200px;
    overflow: hidden;
    background: var(--backdrop);
    font-family: "Jost", "Futura", sans-serif;
  }
  .canvas {
    width: 1200px;
    height: 1200px;
    display: flex;
    align-items: center;
    justify-content: center;
  }
  .sign {
    position: relative;
    width: 1004px;
    height: 627px;
    display: flex;
    flex-direction: column;
    background: var(--white);
    overflow: hidden;
  }
  .band-navy {
    background: linear-gradient(90deg, var(--navy-deep) 0%, var(--navy-mid) 55%, var(--navy-light) 100%);
    color: var(--white);
  }
  .brand-band {
    height: 284px;
    display: flex;
    flex-direction: column;
    align-items: center;
    justify-content: center;
    text-align: center;
    font-weight: 400;
  }
  .brand-line {
    display: flex;
    align-items: center;
    gap: 22px;
  }
  .brand-dot {
    width: 58px;
    height: 58px;
    border-radius: 50%;
    background: var(--gold);
    flex: none;
  }
  .brand-name {
    font-size: 90px;
    line-height: 1;
    letter-spacing: 1px;
  }
  .brand-sub {
    margin-top: 28px;
    font-size: 64px;
    line-height: 1;
    letter-spacing: 40px;
    padding-left: 40px;
    font-weight: 400;
  }
  .contact-band {
    position: relative;
    height: 227px;
    display: flex;
    flex-direction: column;
    align-items: center;
    justify-content: center;
    color: var(--ink);
    z-index: 1;
  }
  .contact-line {
    display: flex;
    align-items: center;
    gap: 22px;
    font-size: 56px;
    font-weight: 500;
    line-height: 1;
  }
  .phone-icon { width: 60px; height: 60px; flex: none; }
  .contact-number {
    margin-top: 14px;
    font-size: 104px;
    font-weight: 600;
    line-height: 1;
    letter-spacing: 1px;
  }
  .web-band {
    height: 116px;
    display: flex;
    align-items: center;
    justify-content: center;
    font-size: 36px;
    font-weight: 300;
    letter-spacing: 0.5px;
  }
  .web-band strong { font-weight: 600; }
  .deco-circle {
    position: absolute;
    right: 42px;
    top: 270px;
    width: 190px;
    height: 190px;
    border-radius: 50%;
    background: var(--faint);
    z-index: 0;
  }
  .corner-circle {
    position: absolute;
    left: 18px;
    bottom: 18px;
    width: 96px;
    height: 96px;
    border-radius: 50%;
    background: var(--navy-deep);
    border: 4px solid var(--white);
    z-index: 2;
  }
</style>
</head>
<body>
<main class="canvas">
  <section class="sign">
    <header class="brand-band band-navy">
      <div class="brand-line">
        <span class="brand-dot" aria-hidden="true"></span>
        <span class="brand-name">TIDEWATER RIDGE</span>
      </div>
      <div class="brand-sub">HOMES</div>
    </header>
    <div class="deco-circle" aria-hidden="true"></div>
    <div class="contact-band">
      <div class="contact-line">
        <svg class="phone-icon" viewBox="0 0 70 70" aria-hidden="true">
          <defs>
            <linearGradient id="goldFill" x1="0" y1="0" x2="0" y2="1">
              <stop offset="0" stop-color="#f7c21a"/>
              <stop offset="1" stop-color="#d99a00"/>
            </linearGradient>
          </defs>
          <circle cx="35" cy="35" r="34" fill="url(#goldFill)"/>
          <path d="M24 19c1.5-1 3.5-.8 4.5.8l3 5c.8 1.3.5 3-.7 4l-2 1.6c1.6 3.6 4.4 6.5 8 8.2l1.7-2c1-1.2 2.7-1.5 4-.7l5 3c1.6 1 1.8 3.1.7 4.6l-2 2.6c-1.4 1.8-3.8 2.4-6 1.6C30 48.6 21.5 40 18.3 29.9c-.7-2.2-.1-4.6 1.700-6z" fill="none" stroke="#fff" stroke-width="2.6" stroke-linejoin="round"/>
          <path d="M39 21a11 11 0 0 1 10 10M39 15a17 17 0 0 1 16 16" fill="none" stroke="#fff" stroke-width="2.4" stroke-linecap="round"/>
        </svg>
        <span>CONTACT US ON</span>
      </div>
      <div class="contact-number">021-574-3619</div>
    </div>
    <footer class="web-band band-navy">
      <span>WWW.<strong>TIDEWATERRIDGEHOMES</strong>.COM</span>
    </footer>
    <div class="corner-circle" aria-hidden="true"></div>
  </section>
</main>
</body>
</html>
```